International Legal Service Company needs Letterhead Design

Put my new Logo into Letterhead Design, using updated telephone number, e-mail address and website. Current letterhead and updated information which i want you to include my new letterhead attached herewith. Of course, my new Logo attached herein. Also, you can use slogan "Total Legal Outsourcing Solutions For Multinational Businesses"

It Company

```html
<!DOCTYPE html>
<html lang="en">
<head>
<meta charset="utf-8">
<title>Meridian Counsel Partners Inc — Letterhead</title>
<link rel="stylesheet" href="https://fonts.googleapis.com/css2?family=Open+Sans:wght@400;600&display=swap">
<style>
  :root {
    --backdrop: #e9e9ea;
    --paper: #f8f8f8;
    --ink: #5d6066;
    --ink-soft: #7a7d83;
    --navy: #1f3f7a;
    --navy-dark: #2a4680;
    --sky: #8dbbe6;
    --rule: #9a9ca1;
    --signature-tone: #ececee;
  }
  * { box-sizing: border-box; margin: 0; padding: 0; }
  html, body { width: 1200px; height: 1000px; overflow: hidden; }
  body {
    background: var(--backdrop);
    font-family: "Open Sans", Arial, sans-serif;
    color: var(--ink);
  }
  .letterhead {
    position: absolute;
    left: 282px;
    top: 50px;
    width: 636px;
    height: 900px;
    background: var(--paper);
    box-shadow: 0 2px 10px rgba(0,0,0,0.08);
  }
  .top-accent {
    position: absolute;
    top: 0;
    left: 96px;
    display: flex;
    gap: 8px;
  }
  .top-accent span { display: block; width: 13px; height: 42px; }
  .top-accent .accent-light { background: var(--sky); }
  .top-accent .accent-dark { background: var(--navy-dark); }

  .brand {
    position: absolute;
    top: 112px;
    left: 268px;
    display: flex;
    align-items: center;
    gap: 10px;
  }
  .brand-dot {
    width: 46px; height: 46px; border-radius: 50%;
    background: var(--navy);
  }
  .brand-name {
    font-weight: 600;
    font-size: 16px;
    line-height: 1.15;
    color: var(--navy);
    width: 170px;
  }

  .letter-body {
    position: absolute;
    top: 200px;
    left: 64px;
    width: 470px;
    font-size: 9.5px;
    line-height: 1.55;
    color: var(--ink);
  }
  .letter-body p { margin-bottom: 24px; text-align: justify; }
  .letter-body .salutation, .letter-body .closing { margin-bottom: 10px; text-align: left; }

  .signature {
    position: absolute;
    top: 620px;
    left: 300px;
    width: 150px;
    height: 44px;
    background: var(--signature-tone);
    border-radius: 4px;
  }

  .contact-block {
    position: absolute;
    top: 786px;
    left: 190px;
    display: flex;
    font-size: 8.5px;
    line-height: 1.35;
    color: var(--ink-soft);
  }
  .contact-address { width: 120px; padding-right: 10px; position: relative; }
  .contact-address .bar { display: block; width: 130px; height: 9px; background: var(--sky); margin-top: 14px; margin-left: -10px; }
  .contact-divider { width: 1px; background: var(--rule); margin-right: 10px; }
  .contact-lines { width: 160px; padding-top: 30px; }
  .contact-lines .bar { display: block; width: 150px; height: 9px; background: var(--navy-dark); margin-top: 8px; }
  .contact-row { display: flex; align-items: center; gap: 5px; }
  .contact-row svg { width: 8px; height: 8px; flex: none; fill: var(--sky); }
</style>
</head>
<body>
  <main class="letterhead">
    <div class="top-accent"><span class="accent-light"></span><span class="accent-dark"></span></div>

    <header class="brand">
      <span class="brand-dot"></span>
      <span class="brand-name">Meridian Counsel Partners Inc</span>
    </header>

    <section class="letter-body">
      <p class="salutation">Dear Client,</p>
      <p>Lorem ipsum dolor sit amet, consectetur adipiscing elit. Nulla sodales nisi vitae lorem ipsum dolor sit amet, consectetur adipiscing elit. Suspendisse feugiat eros nisi, a facilisis risus eleifend sed. Aliquam mauris enim, fermentum eu lacinia sit amet, laoreet eu leo. Nullam eleifend nulla in libero tristique, ac vulputate odio tincidunt. Etiam non condimentum tortor. Integer suscipit neque nec odio porttitor cursus. Phasellus a sapien blandit, suscipit justo in, condimentum ante. Morbi tristique justo risus, id mattis dui molestie ut. Nullam volutpat ut quam commodo faucibus. Pellentesque urna est, interdum in elit quis, pharetra elementum orci. Nam pharetra velit molestie justo placerat scelerisque.</p>
      <p>Nulla tincidunt molestie libero vel pretium. Donec condimentum nulla sit amet risus semper imperdiet. Duis congue eros nec diam blandit, et pellentesque sapien auctor. Curabitur iaculis enim lectus, in imperdiet mauris mattis eget. Etiam ac ornare metus. Mauris risus leo, egestas at dolor a, ultrices adipiscing est. Nunc faucibus scelerisque mollis. Pellentesque aliquet mauris tellus, id dignissim risus viverra et. Mauris venenatis lobortis eros. Nam id diam in ligula malesuada feugiat. Cras turpis felis, aliquet id mauris elementum, feugiat ultricies nisl.</p>
      <p>Nullam auctor venenatis metus, eu pulvinar sapien dapibus non. Cum sociis natoque penatibus et magnis dis parturient montes, nascetur ridiculus mus. Praesent sed lorem eget tortor volutpat dictum vel vel ipsum. Morbi ac mauris sed elit dictum volutpat. Morbi pulvinar non nisi in ultrices. Pellentesque quis mi in risus eleifend adipiscing.</p>
      <p class="closing">Best regards,</p>
    </section>

    <div class="signature" role="img" aria-label="Handwritten signature of Haruto Sakamoto"></div>

    <footer class="contact-block">
      <div class="contact-address">
        <div class="contact-row">
          <svg viewBox="0 0 10 10" aria-hidden="true"><path d="M5 0a3.5 3.5 0 0 0-3.5 3.5C1.5 6 5 10 5 10s3.5-4 3.5-6.5A3.5 3.5 0 0 0 5 0zm0 5a1.5 1.5 0 1 1 0-3 1.5 1.5 0 0 1 0 3z"/></svg>
          <span>418 Harbor View Drive</span>
        </div>
        <div style="padding-left:13px">Suite 210<br>Fairmont,<br>MD 20731</div>
        <span class="bar"></span>
      </div>
      <div class="contact-divider"></div>
      <div class="contact-lines">
        <div class="contact-row">
          <svg viewBox="0 0 10 10" aria-hidden="true"><path d="M2 0l2 2.5-1 1.2c.7 1.4 1.8 2.5 3.2 3.2l1.2-1L10 8l-1 2C4.5 10 0 5.5 0 1z"/></svg>
          <span>240-555-0147</span>
        </div>
        <div class="contact-row">
          <svg viewBox="0 0 10 10" aria-hidden="true"><rect x="0" y="2" width="10" height="6" rx="1"/></svg>
          <span>240-555-0182</span>
        </div>
        <div class="contact-row">
          <svg viewBox="0 0 10 10" aria-hidden="true"><path d="M0 2h10v6H0z M0 2l5 3.5L10 2" /></svg>
          <span>hsakamoto@meridiancounsel.net</span>
        </div>
        <div class="contact-row">
          <svg viewBox="0 0 10 10" aria-hidden="true"><circle cx="5" cy="5" r="5"/></svg>
          <span>meridiancounsel.net</span>
        </div>
        <span class="bar"></span>
      </div>
    </footer>
  </main>
</body>
</html>
```